Packaging design for a revolutionary hi-protein snack of Norwegian salmon

We need a breathtaking packing design for a smal snack bag (30 g) for a revolutionary new hi-protein snack made of Norwegian salmon. The product will be made with two different flavors; MANGO and WASABI. The product is extreme high in protein (60%) and omega 3, and are just natural.

We want to see a bold and fresh design that appeals to protein lovers of all ages.

Target Market(s)

Our target market is boys and girls that are 18-35 years old and that are interested in working out and eating healthy.

Industry/Entity Type

Snack industry (functional food, healthy snack, protein snack)

Font styles to use
Sans Serif

Requirements
Must have
• The package design must give the customer a WOW feeling. "HI-PROTEIN SNACK" must be highligted. Further, the design must use the Tidal Compass setup (attached).

```html
<!DOCTYPE html>
<html lang="en">
<head>
<meta charset="utf-8">
<title>Tidal Compass Hi-Protein Snack</title>
<link rel="stylesheet" href="https://fonts.googleapis.com/css2?family=Oswald:wght@600;700&family=Montserrat:wght@600;700&display=swap">
<style>
  :root{
    --backdrop:#a9a9a9;
    --bag-white:#ffffff;
    --ink:#141414;
    --mango:#f3cf1f;
    --mango-deep:#e6b800;
    --wasabi:#8fd11f;
    --wasabi-deep:#6fb80e;
    --rule:#e4e4e4;
    --salmon-a:#f08a3c;
    --salmon-b:#c9532a;
  }
  *{box-sizing:border-box;margin:0;padding:0}
  html,body{width:1200px;height:1200px;overflow:hidden}
  body{background:var(--backdrop);position:relative;font-family:"Montserrat",sans-serif}
  .pack{
    position:absolute;top:250px;width:480px;height:700px;
    background:var(--bag-white);
    overflow:hidden;
  }
  .pack--mango{left:70px;--accent:var(--mango);--accent-deep:var(--mango-deep)}
  .pack--wasabi{left:650px;--accent:var(--wasabi);--accent-deep:var(--wasabi-deep)}
  .pack__lines{
    position:absolute;inset:0;
    background:repeating-linear-gradient(180deg,transparent 0 13px,var(--rule) 13px 14px);
    opacity:.7;
  }
  .seal{position:absolute;left:0;right:0;height:28px;background:#f6f6f6}
  .seal--top{top:0}
  .seal--bottom{bottom:0;background:var(--accent-deep)}
  .hang-hole{position:absolute;top:10px;left:232px;width:16px;height:10px;border:2px solid #c8c8c8;border-radius:0 0 8px 8px;background:var(--backdrop)}
  .header-stripes{position:absolute;top:60px;left:0;right:0;height:40px}
  .header-stripes span{position:absolute;height:6px;background:var(--accent)}
  .brand{
    position:absolute;top:48px;left:0;right:0;text-align:center;
    font-family:"Montserrat",sans-serif;font-weight:700;font-size:24px;line-height:1;color:var(--ink);
  }
  .brand__dot{display:inline-block;width:10px;height:10px;border-radius:50%;background:var(--ink);margin-left:6px;vertical-align:middle}
  .headline{
    position:absolute;top:120px;left:50px;
    font-family:"Oswald",sans-serif;font-weight:700;line-height:.95;letter-spacing:1px;
  }
  .headline__top{display:block;font-size:60px;color:var(--ink)}
  .headline__bottom{display:block;font-size:60px;color:var(--accent-deep)}
  .flavour{
    position:absolute;top:285px;right:0;width:250px;height:80px;
    background:var(--accent);
    font-family:"Oswald",sans-serif;font-weight:700;font-size:34px;letter-spacing:2px;color:var(--ink);
    display:flex;align-items:center;padding-left:48px;
  }
  .wave{position:absolute;left:0;bottom:0;width:480px;height:250px}
  .product-photo{
    position:absolute;top:380px;left:70px;width:170px;height:190px;border-radius:40% 50% 45% 40%;
    background:radial-gradient(circle at 40% 40%,var(--salmon-a),var(--salmon-b));
  }
  .natural{position:absolute;top:395px;left:255px;width:190px;height:70px}
  .natural__label{
    position:absolute;top:50px;left:24px;font-weight:700;font-size:15px;color:var(--accent-deep);white-space:nowrap;
  }
  .claim{
    position:absolute;top:585px;left:60px;right:60px;height:36px;background:var(--ink);
    color:var(--accent);font-weight:700;font-size:14px;display:flex;align-items:center;justify-content:center;letter-spacing:.3px;
  }
  .weight{position:absolute;top:632px;left:0;right:0;text-align:center;font-weight:600;font-size:24px;color:var(--ink)}
</style>
</head>
<body>

<section class="pack pack--mango">
  <div class="pack__lines"></div>
  <svg class="wave" viewBox="0 0 480 250" aria-hidden="true">
    <path d="M0 70 L130 50 L220 80 L480 20 L480 250 L0 250 Z" fill="var(--accent)"/>
    <path d="M0 58 L130 38 L220 68 L480 8" fill="none" stroke="var(--accent)" stroke-width="6"/>
  </svg>
  <div class="seal seal--top"></div>
  <div class="seal seal--bottom"></div>
  <div class="hang-hole"></div>
  <div class="header-stripes">
    <span style="left:0;width:150px;top:18px"></span>
    <span style="left:0;width:150px;top:30px"></span>
    <span style="right:0;width:150px;top:0"></span>
    <span style="right:0;width:150px;top:12px"></span>
  </div>
  <div class="brand">Tidal<br>Compass<span class="brand__dot"></span></div>
  <h1 class="headline"><span class="headline__top">HI-PROTEIN</span><span class="headline__bottom">SNACK</span></h1>
  <div class="flavour">MANGO</div>
  <div class="product-photo" role="img" aria-label="Photo of dried salmon snack pieces"></div>
  <div class="natural">
    <svg width="80" height="50" viewBox="0 0 80 50" aria-hidden="true">
      <path d="M4 30 C20 4 52 4 62 30" fill="none" stroke="var(--accent-deep)" stroke-width="4" stroke-linecap="round"/>
      <path d="M52 26 L62 36 L70 24" fill="none" stroke="var(--accent-deep)" stroke-width="4" stroke-linecap="round" stroke-linejoin="round"/>
    </svg>
    <span class="natural__label">JUST NATURAL</span>
  </div>
  <p class="claim">HIGH IN PROTEIN (60%) AND OMEGA 3</p>
  <p class="weight">30 g</p>
</section>

<section class="pack pack--wasabi">
  <div class="pack__lines"></div>
  <svg class="wave" viewBox="0 0 480 250" aria-hidden="true">
    <path d="M0 70 L130 50 L220 80 L480 20 L480 250 L0 250 Z" fill="var(--accent)"/>
    <path d="M0 58 L130 38 L220 68 L480 8" fill="none" stroke="var(--accent)" stroke-width="6"/>
  </svg>
  <div class="seal seal--top"></div>
  <div class="seal seal--bottom"></div>
  <div class="hang-hole"></div>
  <div class="header-stripes">
    <span style="left:0;width:150px;top:18px"></span>
    <span style="left:0;width:150px;top:30px"></span>
    <span style="right:0;width:150px;top:0"></span>
    <span style="right:0;width:150px;top:12px"></span>
  </div>
  <div class="brand">Tidal<br>Compass<span class="brand__dot"></span></div>
  <h1 class="headline"><span class="headline__top">HI-PROTEIN</span><span class="headline__bottom">SNACK</span></h1>
  <div class="flavour">WASABI</div>
  <div class="product-photo" role="img" aria-label="Photo of dried salmon snack pieces"></div>
  <div class="natural">
    <svg width="80" height="50" viewBox="0 0 80 50" aria-hidden="true">
      <path d="M4 30 C20 4 52 4 62 30" fill="none" stroke="var(--accent-deep)" stroke-width="4" stroke-linecap="round"/>
      <path d="M52 26 L62 36 L70 24" fill="none" stroke="var(--accent-deep)" stroke-width="4" stroke-linecap="round" stroke-linejoin="round"/>
    </svg>
    <span class="natural__label">JUST NATURAL</span>
  </div>
  <p class="claim">HIGH IN PROTEIN (60%) AND OMEGA 3</p>
  <p class="weight">30 g</p>
</section>

</body>
</html>
```